Pelmoro Travel

We are new traveling company from Italy and looking for a really unique design as soon as possible of the main page.
Travel is an online business. We all do online research before taking a vacation. Since some of us will spend hours researching a trip before finally booking it on a travel website, design is critical.
People looking to travel are going to start with an idea. Some may be browsing for a specific type of trip (river cruise, kayaking, etc.) while others may be looking at specific dates (i.e. February). Still others are considering going to a specific destination such as the Grand Canyon, but all of these visitors are goal-oriented. This type of visitor is frustrated by not finding thle right information easily. This is why travel web design must offer several ways to navigate such as by date, location, activity, cost, etc.
The design should be easy to use for visitors, look fantastic and be easy to update and maintain.
Uploaded some sample pictures but feel free to use your own if it looks good. About colors, blue and white would mix great.

Our future address will be pelmorotravel.com

```html
<!DOCTYPE html>
<html lang="en">
<head>
<meta charset="utf-8">
<title>Pelmoro Travel</title>
<link href="https://fonts.googleapis.com/css2?family=Open+Sans:ital,wght@0,400;0,600;1,400&display=swap" rel="stylesheet">
<style>
:root{
  --blue:#1f6fc0;
  --blue-dark:#1859a8;
  --band-top:#3fa2e6;
  --band-bottom:#2379c8;
  --orange:#f7a300;
  --orange-light:#ffbf1e;
  --text:#333;
  --muted:#8a8a8a;
  --line:#dcdcdc;
  --field:#f4f4f4;
}
*{box-sizing:border-box;margin:0;padding:0}
html,body{width:747px;height:1200px;overflow:hidden;background:#fff}
body{position:relative;font-family:"Open Sans",Arial,sans-serif;color:var(--text)}
.abs{position:absolute}
.brand{left:58px;top:19px;font-weight:600;font-size:21px;color:var(--blue)}
.search{left:526px;top:24px;width:162px;height:20px;border:1px solid #c9c9c9;border-radius:10px;font-size:7px;font-style:italic;color:#777;padding:5px 10px}
.search svg{position:absolute;right:7px;top:4px}
.nav{left:0;top:59px;width:747px;height:35px;background:linear-gradient(#2d86d4,var(--blue-dark))}
.nav a{position:absolute;top:11px;font-size:11px;color:#fff;text-decoration:none;text-transform:uppercase}
.nav .sep{position:absolute;top:0;width:1px;height:35px;background:rgba(0,0,0,.18);box-shadow:1px 0 rgba(255,255,255,.12)}
.hero{left:0;top:94px;width:747px;height:298px;background:linear-gradient(180deg,#7fb8dc 0%,#4f8a74 30%,#2ec4cf 48%,#27b9c4 62%,#d9d4c4 80%,#7aa36a 100%)}
.hero h1{position:absolute;left:0;width:747px;top:118px;text-align:center;font-weight:600;font-size:26px;color:#fff;text-shadow:0 1px 3px rgba(0,0,0,.3)}
.hero p{position:absolute;left:0;width:747px;top:154px;text-align:center;font-size:22px;color:#fff;text-shadow:0 1px 3px rgba(0,0,0,.3)}
.dots{left:351px;top:282px;display:flex;gap:4px}
.dots i{width:8px;height:8px;border-radius:50%;background:#fff;opacity:.9}
.band{left:0;top:392px;width:747px;height:102px;background:linear-gradient(var(--band-top),var(--band-bottom))}
.band .div{position:absolute;top:12px;width:1px;height:70px;background:rgba(255,255,255,.3)}
.feat h3{position:absolute;top:18px;font-weight:400;font-size:15px;color:#fff;white-space:nowrap}
.feat p{position:absolute;top:37px;font-size:8.3px;line-height:13px;color:#eaf4fc;width:122px}
.feat .btn{position:absolute;top:68px;width:62px;height:17px;background:#5bb6f0;color:#fff;font-size:7.5px;text-align:center;line-height:17px;text-transform:uppercase}
.welcome h2{position:absolute;left:62px;top:530px;font-weight:400;font-size:19px;color:#222}
.welcome p{position:absolute;left:64px;width:412px;font-size:8px;line-height:13.6px;color:#555}
.section-title{left:61px;top:665px;font-size:16px;color:var(--blue);font-weight:400}
.tour{position:absolute;width:135px}
.tour .ph{width:135px;height:67px}
.tour h4{font-weight:400;font-size:10.5px;color:#333;margin-top:7px}
.tour p{font-size:8px;line-height:12.4px;color:var(--muted);margin-top:1px}
.tour time{display:block;font-size:8px;color:var(--blue);margin-top:2px}
.quote{left:505px;top:513px;width:177px;height:200px;border:1px solid var(--line);border-radius:3px}
.quote .head{height:31px;background:linear-gradient(var(--orange-light),var(--orange));color:#fff;font-size:12px;padding:8px 14px;border-radius:2px 2px 0 0}
.field{position:absolute;height:19px;border:1px solid #d3d3d3;background:var(--field);border-radius:2px;font-size:7.5px;color:#555;padding:5px 8px}
.submit{position:absolute;left:12px;top:161px;width:68px;height:22px;background:linear-gradient(#2f86d8,var(--blue-dark));border-radius:2px;color:#fff;font-size:10px;font-weight:600;text-align:center;line-height:22px}
.testi{left:505px;top:726px;width:177px;height:215px;border:1px solid var(--line);border-radius:3px}
.testi .head{height:31px;background:linear-gradient(#fafafa,#efefef);border-bottom:1px solid var(--line);font-size:12px;color:#333;padding:8px 17px;text-transform:uppercase}
.testi blockquote{position:absolute;left:19px;width:150px;font-style:italic;font-size:7.9px;line-height:13.5px;color:#888}
.testi cite{position:absolute;left:19px;font-style:normal;font-size:7.8px;color:#333}
.footer{left:0;top:1002px;width:747px;height:198px;background:linear-gradient(#fff,#f4f4f4);border-top:1px solid #e2e2e2}
.fcol{position:absolute;top:27px}
.fcol h5{font-weight:400;font-size:13.5px;color:var(--blue);margin-bottom:5px}
.fcol li{list-style:none;font-size:8.6px;line-height:14.7px;color:#444}
.social{display:flex;gap:6px;margin-top:4px}
.social i{width:16px;height:16px;border-radius:2px}
.bottom{left:0;top:1161px;width:747px;height:39px;border-top:1px solid #e0e0e0;background:#f6f6f6}
.bottom p{position:absolute;left:61px;top:13px;font-size:8px;color:#555}
</style>
</head>
<body>

<div class="abs brand">Pelmoro Travel</div>
<div class="abs search">Search here..
  <svg width="11" height="11" viewBox="0 0 11 11"><circle cx="4.5" cy="4.5" r="3.3" fill="none" stroke="#888" stroke-width="1.4"/><line x1="7" y1="7" x2="10" y2="10" stroke="#888" stroke-width="1.6"/></svg>
</div>

<nav class="abs nav">
  <a style="left:73px">Home</a><span class="sep" style="left:118px"></span>
  <a style="left:133px">About Us</a><span class="sep" style="left:197px"></span>
  <a style="left:213px">Research Trip</a><span class="sep" style="left:301px"></span>
  <a style="left:318px">Location</a><span class="sep" style="left:382px"></span>
  <a style="left:398px">Activity</a><span class="sep" style="left:455px"></span>
  <a style="left:470px">Costs</a><span class="sep" style="left:515px"></span>
  <a style="left:531px">Testimonials</a><span class="sep" style="left:617px"></span>
  <a style="left:633px">Contact</a>
</nav>

<section class="abs hero" role="img" aria-label="Tropical lagoon with overwater bungalows, turquoise sea, mountains, palm trees and beach">
  <h1>BOOK YOUR TRIP NOW</h1>
  <p>PRAESENT VITAE LACUS VELIT VESTIBULUM</p>
  <div class="abs dots"><i></i><i></i><i></i><i></i></div>
</section>

<section class="abs band">
  <div class="feat">
    <svg class="abs" style="left:75px;top:20px" width="32" height="32" viewBox="0 0 32 32"><circle cx="13" cy="13" r="9" fill="none" stroke="#fff" stroke-width="4"/><line x1="20" y1="20" x2="29" y2="29" stroke="#fff" stroke-width="5" stroke-linecap="round"/></svg>
    <h3 style="left:115px">Find a Trip Vocation</h3>
    <p style="left:116px">Vivamus porttitor g purus nisi eleifend libero tempus</p>
    <div class="btn" style="left:116px">Read More</div>
  </div>
  <div class="div" style="left:265px"></div>
  <div class="feat">
    <svg class="abs" style="left:295px;top:20px" width="34" height="34" viewBox="0 0 34 34"><path d="M3 5h18v8M21 22v9H3V5" fill="none" stroke="#fff" stroke-width="2.4"/><line x1="7" y1="12" x2="16" y2="12" stroke="#fff" stroke-width="2"/><line x1="7" y1="17" x2="14" y2="17" stroke="#fff" stroke-width="2"/><line x1="7" y1="22" x2="12" y2="22" stroke="#fff" stroke-width="2"/><path d="M29 8l3 3-13 14-4 1 1-4z" fill="#fff"/></svg>
    <h3 style="left:339px">Online Research</h3>
    <p style="left:339px">Vivamus porttitor g purus nisi eleifend libero tempus</p>
    <div class="btn" style="left:339px;top:67px">Read More</div>
  </div>
  <div class="div" style="left:478px"></div>
  <div class="feat">
    <svg class="abs" style="left:497px;top:22px" width="42" height="32" viewBox="0 0 42 32"><rect x="6" y="2" width="30" height="20" fill="none" stroke="#fff" stroke-width="2.4"/><path d="M1 26h40l-3 4H4z" fill="#fff"/></svg>
    <h3 style="left:550px">Book a Trip Now</h3>
    <p style="left:550px">Vivamus porttitor g purus nisi eleifend libero tempus liber</p>
    <div class="btn" style="left:551px;top:67px">Read More</div>
  </div>
</section>

<section class="welcome">
  <h2>Welcome to Our Website Mainpage</h2>
  <p style="top:560px">Morbi ornare gravida elit Integer congue augue et malesuada iaculis ipsum dui aliquet felis at cursus magna nisl nec elit Donec iaculis diam a nisi accumsan viverra Duis sed tellus et tortor vestibulum gravida Praesent elementum elit at tellus Curabitur metus ipsum luctus eu malesuada ut tincidunt sed diam</p>
  <p style="top:604px">Donec quis mi sed magna hendrerit accumsan Suspendisse risus nibh ultricies eu volutpat non condimentum hendrerit augue Etiam eleifend metus vitae adipiscing semper mauris ipsum iaculis eli</p>
</section>

<h3 class="abs section-title">Recent Tours &amp; Trips</h3>

<article class="tour" style="left:61px;top:694px"><div class="ph" role="img" aria-label="Palm tree over a beach and blue sky" style="background:linear-gradient(#5fa6e0,#bfe0f2 55%,#3fb0c8)"></div><h4>Suspendisse risus nibh</h4><p>ultricies eu volutpat non condimen-tum hendrerit augue Etiam elei</p><time>25 April 2014</time></article>
<article class="tour" style="left:206px;top:694px"><div class="ph" role="img" aria-label="Turquoise bay with green hills" style="background:linear-gradient(#6fb4e6,#2a8fc0 45%,#3cc3c9)"></div><h4>Maecenas justo</h4><p>ultricies eu volutpat non condimen-tum hendrerit augue Etiam elei</p><time>25 April 2014</time></article>
<article class="tour" style="left:348px;top:694px"><div class="ph" role="img" aria-label="Island on the horizon under clouds" style="background:linear-gradient(#2f6fc4,#c9e2f4 55%,#4ab4c6)"></div><h4>Nam cursus Morbi</h4><p>ultricies eu volutpat non condimen-tum hendrerit augue Etiam elei</p><time>25 April 2014</time></article>
<article class="tour" style="left:60px;top:840px"><div class="ph" role="img" aria-label="Sandy cove with clear water" style="background:linear-gradient(#2f7fb0,#1d5e7a 40%,#38b5c8 70%,#e7dcc0)"></div><h4>Phasellus felis dolor</h4><p>ultricies eu volutpat non condimen-tum hendrerit augue Etiam elei</p><time>25 April 2014</time></article>
<article class="tour" style="left:205px;top:840px"><div class="ph" role="img" aria-label="Palm trees on a sunny beach" style="background:linear-gradient(#4a90d4,#9ccbea 45%,#6a9a4a 80%,#e2d7b8)"></div><h4>Donec convallis pede</h4><p>ultricies eu volutpat non condimen-tum hendrerit augue Etiam elei</p><time>25 April 2014</time></article>
<article class="tour" style="left:348px;top:840px"><div class="ph" role="img" aria-label="Overwater bungalows in a lagoon" style="background:linear-gradient(#5fb0e0,#34c0d0 50%,#2aa8c0)"></div><h4>Morbi eget arcu</h4><p>ultricies eu volutpat non condimen-tum hendrerit augue Etiam elei</p><time>25 April 2014</time></article>

<aside class="abs quote">
  <div class="head">GET A TRIP QUOTE</div>
  <div class="field" style="left:11px;top:41px;width:154px">Your Name</div>
  <div class="field" style="left:11px;top:64px;width:154px">Email address</div>
  <div class="field" style="left:11px;top:88px;width:154px">Location Area Trip</div>
  <div class="field" style="left:11px;top:112px;width:75px">Book In Time</div>
  <div class="field" style="left:90px;top:112px;width:75px">Out Time</div>
  <div class="field" style="left:11px;top:137px;width:154px">Phone no.</div>
  <div class="submit">Submit</div>
</aside>

<aside class="abs testi">
  <div class="head">Testimonials</div>
  <blockquote style="top:40px">Etiam est nunc venenatis in tristique eu imperdiet ac nisl Cum sociis natoque penatibus et magnis dis parturient montes nascetur ridiculus mus In iaculis facilisis massa Etiam eu urna Sed porta</blockquote>
  <cite style="top:113px">By Author Name</cite>
  <blockquote style="top:133px">Duis non nunc Nulla rhoncus dictum metus Curabitur tristique mi condimen-tum orci Phasellus pellentesque aliquam enim Proin dui lectus cursus</blockquote>
  <cite style="top:189px">By Author Name</cite>
</aside>

<footer class="abs footer">
  <div class="fcol" style="left:62px"><h5>Company</h5><ul><li>About Company</li><li>Why Choose Us</li><li>How it works</li><li>Reviews Trips</li><li>Offers</li></ul></div>
  <div class="fcol" style="left:190px"><h5>Services</h5><ul><li>Etiam est nunc</li><li>Venenatis tristique</li><li>Eu imperdiet ac nisl</li><li>Cum sociis</li><li>Natoque</li></ul></div>
  <div class="fcol" style="left:315px"><h5>Special Offer</h5><ul><li>Open an individual account</li><li>Open a business account</li><li>Other services</li><li>Refer a friend</li><li>Affiliates</li></ul></div>
  <div class="fcol" style="left:456px"><h5>Support</h5><ul><li>FAQ</li><li>Customer Support</li><li>Resources</li><li>Advices &amp; Use</li><li>Contact</li></ul></div>
  <div class="fcol" style="left:574px"><h5>Get in touch</h5>
    <div class="social"><i style="background:#3b5a98"></i><i style="background:#4fb3e6"></i><i style="background:#1a6fa8"></i><i style="background:#f07a1a"></i></div>
  </div>
</footer>

<div class="abs bottom"><p>© 2014 Company Name&nbsp; All right reserved&nbsp; Term of Use</p></div>

</body>
</html>
```